VEXO requires an exciting new business card

New business card required for VEXO. We are a new market research consultancy and want our brand to be approachable and be contemporary/modern, bold, uncomplicated/simple, and use friendly and easy to read fonts.

A draft website front page is attached to give you a feel (the pictures will be improved over the coming days).

The business card will be printed on 600gsm card, full colour both sides. The card is unique in that it allows one of four colours to be placed within the seam of the card (see http://uk.tarnix.com/products/halo/business-cards.html)

The logo has been designed in yellow on white, white on yellow, yellow on black and black on yellow - please select whichever you feel most appropriate from the attached document (please use the versions with the tagline). I think my preference is yellow on white for the front, and then yellow or black as the dominant colour on the back.

Telephone numbers will be given next week as they are now being finalised.

Thanks

Target Market(s)

Professionals in large corporates, such as Marketing Managers at Bravik, Fizzor Dune, Domacore etc.

Industry/Entity Type

Market Research

Requirements
Must have
• Greg Hallow QPMR
vexo
Level 4, 17 Ember St
Quindle Park
NSW 2087
Tel: 02 XXXX XXXX
Mob: XXXX XXXXXX
Email: greg@vexomr.com.au
Web: www.vexomr.com.au

```html
<!DOCTYPE html>
<html lang="en">
<head>
<meta charset="utf-8">
<title>vexo — business card</title>
<link rel="stylesheet" href="https://fonts.googleapis.com/css2?family=Montserrat:wght@400;600;700&display=swap">
<style>
  :root {
    --yellow: #f9c53c;
    --charcoal: #3d3d3d;
    --ink-soft: #7a7a7a;
    --paper: #ffffff;
    --stage-edge: #e9e9e9;
  }
  * { margin: 0; padding: 0; box-sizing: border-box; }
  html, body { width: 1200px; height: 900px; overflow: hidden; background: var(--paper); }
  body { font-family: "Montserrat", sans-serif; position: relative; }

  .stage {
    position: absolute; left: 0; top: 0; width: 1200px; height: 695px;
    background: radial-gradient(ellipse 700px 420px at 600px 360px, #ffffff 40%, var(--stage-edge) 100%);
  }

  .card { position: absolute; top: 220px; width: 449px; height: 255px; }

  .card-front {
    left: 125px; background: var(--charcoal);
    display: flex; align-items: center; justify-content: center;
  }
  .brand-name {
    font-weight: 700; color: var(--yellow); letter-spacing: -1px;
    display: flex; align-items: center; gap: 6px; line-height: 1;
  }
  .card-front .brand-name { font-size: 44px; margin-top: -4px; }
  .brand-dot { border-radius: 50%; background: currentColor; display: inline-block; }
  .card-front .brand-dot { width: 14px; height: 14px; }

  .card-back {
    left: 621px; background: var(--paper);
    box-shadow: 0 1px 4px rgba(0,0,0,0.25);
  }
  .name-band { position: absolute; left: 0; top: 0; }
  .holder { position: absolute; left: 48px; top: 34px; color: var(--paper); }
  .holder-name { font-size: 20px; font-weight: 400; letter-spacing: 1px; line-height: 24px; }
  .holder-title { font-size: 14px; letter-spacing: 0.5px; line-height: 18px; }

  .contact-list { position: absolute; left: 48px; top: 91px; list-style: none; }
  .contact-list li {
    display: flex; align-items: center; gap: 11px;
    font-size: 12.5px; color: var(--ink-soft); height: 19px;
  }
  .contact-list svg { width: 14px; height: 14px; fill: var(--yellow); flex: none; }

  .address {
    position: absolute; left: 263px; top: 150px; font-style: normal;
    font-size: 12.5px; line-height: 19px; color: var(--ink-soft);
  }

  .footer-brand {
    position: absolute; left: 864px; top: 762px; color: var(--charcoal);
  }
  .footer-brand .brand-name { color: var(--charcoal); font-size: 78px; }
  .footer-brand .brand-dot { width: 24px; height: 24px; }
</style>
</head>
<body>
  <div class="stage">
    <section class="card card-front" aria-label="Card front">
      <span class="brand-name">vexo<span class="brand-dot"></span></span>
    </section>

    <section class="card card-back" aria-label="Card back">
      <svg class="name-band" width="449" height="80" viewBox="0 0 449 80" aria-hidden="true">
        <path d="M0 25 H215 A25 25 0 0 0 240 0 H297 A80 80 0 0 1 217 80 H0 Z" fill="var(--yellow)"/>
      </svg>
      <div class="holder">
        <p class="holder-name">GREG HALLOW</p>
        <p class="holder-title">QPMR</p>
      </div>

      <ul class="contact-list">
        <li>
          <svg viewBox="0 0 16 16" aria-hidden="true"><path d="M3.5 1 L6 1.5 L7 5 L5.2 6.3 Q6.5 9.5 9.7 10.8 L11 9 L14.5 10 L15 12.5 Q14 15 11.5 15 Q2 13 1 4.5 Q1 2 3.5 1Z"/></svg>
          02 XXXX XXXX
        </li>
        <li>
          <svg viewBox="0 0 16 16" aria-hidden="true"><path d="M5 1 H11 Q12.5 1 12.5 2.5 V13.5 Q12.5 15 11 15 H5 Q3.5 15 3.5 13.5 V2.5 Q3.5 1 5 1Z M5 3 V10 H11 V3Z"/></svg>
          XXXX XXXXXX
        </li>
        <li>
          <svg viewBox="0 0 16 16" aria-hidden="true"><path d="M1 3.5 H15 L8 9 Z M1 5 L8 10.5 L15 5 V13 H1 Z"/></svg>
          greg@vexomr.com.au
        </li>
        <li>
          <svg viewBox="0 0 16 16" aria-hidden="true"><path fill-rule="evenodd" d="M8 1 A7 7 0 1 1 7.99 1Z M8 2.6 Q5.6 5 5.6 7.2 H10.4 Q10.4 5 8 2.6Z M5.6 8.8 Q5.6 11 8 13.4 Q10.4 11 10.4 8.8Z M2.7 7.2 H4.2 Q4.3 5 5.6 3.2 Q3.1 4.4 2.7 7.2Z M11.8 7.2 H13.3 Q12.9 4.4 10.4 3.2 Q11.7 5 11.8 7.2Z M2.7 8.8 Q3.1 11.6 5.6 12.8 Q4.3 11 4.2 8.8Z M11.8 8.8 Q11.7 11 10.4 12.8 Q12.9 11.6 13.3 8.8Z"/></svg>
          www.vexomr.com.au
        </li>
      </ul>

      <address class="address">
        vexo<br>
        Level 4, 17 Ember St<br>
        Quindle Park<br>
        NSW 2087
      </address>
    </section>
  </div>

  <div class="footer-brand">
    <span class="brand-name">vexo<span class="brand-dot"></span></span>
  </div>
</body>
</html>
```